themed infographic with multiple stats/charts

**Requires previous infographic experience and examples.**We need a skilled illustrator/designer to take an organized list of stats we've gathered related to the topic of investing and turn them into a professional looking, long, infographic with multiple sections, with a clear visual theme.We are not looking to match our branding guidelines. This will have a style and look all its own, with a goal of being compelling and sharable.Stats/content provided when we engage.

Target Market(s)

US customers, 25-45 years old

Colors

Designer to choose colors to be used in the design.

Requirements
Must have
• interesting theme that ties all the stats together, but separate panels for each stat
Should not have
• will not accept something that looks like cheap clip art

```html
<!DOCTYPE html>
<html lang="en">
<head>
<meta charset="utf-8">
<title>Investing in Your 20's, 30's, 40's, 50's and 60's</title>
<link rel="stylesheet" href="https://fonts.googleapis.com/css2?family=Anton&family=Oswald:wght@300;400;500;600&display=swap">
<style>
  :root {
    --bg-top: #def8f3;
    --bg-bottom: #f1fbfb;
    --blue: #00aeef;
    --navy: #0c2a4e;
    --gold: #f0b23f;
    --ink: #4a5866;
    --tick: #9aa6b2;
    --white: #ffffff;
  }
  * { margin: 0; padding: 0; box-sizing: border-box; }
  html, body { width: 1200px; height: 2861px; overflow: hidden; }
  body {
    position: relative;
    background: linear-gradient(180deg, var(--bg-top) 0%, var(--bg-bottom) 45%, var(--bg-top) 100%);
    font-family: "Oswald", "Arial Narrow", sans-serif;
    color: var(--ink);
  }
  .abs { position: absolute; }

  .title-main {
    left: 50px; top: 66px;
    font-family: "Anton", sans-serif; font-size: 150px; line-height: 1;
    color: var(--blue); white-space: nowrap; letter-spacing: 2px;
  }
  .title-sub {
    left: 50px; top: 208px;
    font-weight: 300; font-size: 97px; line-height: 1;
    color: var(--navy); white-space: nowrap; letter-spacing: 0;
  }

  .tag-row { display: flex; align-items: center; }
  .section-tag {
    height: 53px; padding: 0 44px 0 14px;
    background: var(--navy); color: var(--white);
    font-weight: 500; font-size: 34px; line-height: 53px;
    white-space: nowrap; letter-spacing: 0;
  }
  .section-tag.light { background: var(--white); color: var(--navy); }
  .badge {
    flex: none;
    width: 112px; height: 112px; border-radius: 50%; margin-left: -28px;
    background: var(--gold); color: var(--white);
    font-family: "Anton", sans-serif; font-size: 54px;
    display: flex; align-items: center; justify-content: center;
  }

  .bullets { list-style: none; }
  .bullets li {
    position: relative; padding-left: 27px;
    font-size: 25px; line-height: 29px; font-weight: 400;
    margin-bottom: 7px;
  }
  .bullets li::before {
    content: "✓"; position: absolute; left: 0; top: 7px;
    width: 17px; height: 17px; border-radius: 50%;
    background: var(--tick); color: var(--white);
    font-size: 11px; line-height: 17px; text-align: center; font-weight: 600;
  }
  .bullets.on-dark li { color: var(--white); }
  .bullets.on-dark li::before { background: var(--white); color: var(--navy); }
  .bullets.on-blue li { color: var(--white); }
  .bullets.on-blue li::before { background: var(--white); color: var(--blue); }

  .stat { display: flex; align-items: center; }
  .stat-figure { font-family: "Anton", sans-serif; color: var(--blue); line-height: 1; }
  .stat-note { font-size: 25px; line-height: 29px; margin-left: 14px; }

  .headline {
    font-family: "Anton", sans-serif; color: var(--navy);
    font-size: 78px; line-height: 1; white-space: nowrap;
  }

  .band { left: 0; top: 1060px; width: 1200px; height: 411px; }

  .closing { left: 0; top: 2237px; width: 1200px; height: 624px; }
  .big-white { font-family: "Anton", sans-serif; color: var(--white); font-size: 110px; line-height: 1; }
  .white-note { color: var(--white); font-size: 26px; line-height: 28px; }
</style>
</head>
<body>

  <h1>
    <span class="abs title-main">INVESTING IN YOUR</span>
    <span class="abs title-sub">20'S, 30'S, 40'S, 50'S AND 60'S</span>
  </h1>

  <section>
    <div class="abs tag-row" style="left:31px;top:364px;">
      <div class="section-tag">INVESTING IN YOUR 20'S</div><div class="badge">$</div>
    </div>
    <ul class="abs bullets" style="left:31px;top:478px;width:540px;">
      <li>Start saving</li>
      <li>Start first retirement account</li>
    </ul>
    <div class="abs stat" style="left:29px;top:548px;">
      <span class="stat-figure" style="font-size:108px;">15%</span>
      <span class="stat-note" style="margin-left:24px;width:280px;">Set aside 15% of income in retirement account</span>
    </div>
    <ul class="abs bullets" style="left:31px;top:648px;width:545px;">
      <li>Learn compound interest</li>
      <li>Understand matching 401(k) - average 401k employer contributions growing</li>
    </ul>
  </section>

  <section>
    <div class="abs tag-row" style="left:599px;top:364px;">
      <div class="section-tag">INVESTING IN YOUR 30'S</div><div class="badge">$</div>
    </div>
    <ul class="abs bullets" style="left:599px;top:478px;width:590px;">
      <li>Build emergency fund of 3-6 months worth of expenses</li>
      <li>Increase retirement contributions</li>
      <li>Have equivalent of annual salary saved by age 30</li>
    </ul>
    <div class="abs stat" style="left:599px;top:578px;">
      <span class="stat-figure" style="font-size:108px;">2X</span>
      <span class="stat-note" style="margin-left:22px;width:340px;">Have twice annual salary saved by age 35</span>
    </div>
    <ul class="abs bullets" style="left:599px;top:684px;width:595px;">
      <li>Increase finance knowledge - Understand difference between various investment funds(mutual fund, etf, index)</li>
    </ul>
  </section>

  <section>
    <div class="abs tag-row" style="left:31px;top:779px;">
      <div class="section-tag">INVESTING IN YOUR 40'S</div><div class="badge">$</div>
    </div>
    <ul class="abs bullets" style="left:31px;top:893px;width:560px;">
      <li>Diversify investments</li>
      <li>Keep investment fees low</li>
      <li>Reduce or eliminate debt</li>
      <li>Have 3x your annual salary saved by 40 and 4x by 45</li>
    </ul>
  </section>

  <section>
    <div class="abs tag-row" style="left:599px;top:779px;">
      <div class="section-tag">INVESTING IN YOUR 50'S</div><div class="badge">$</div>
    </div>
    <ul class="abs bullets" style="left:599px;top:893px;width:560px;">
      <li>Avoid new debt</li>
      <li>Take advantage of retirement catch-ups (differences between 401k, IRAs, and HSA)</li>
    </ul>
  </section>

  <svg class="abs band" viewBox="0 0 1200 411" aria-hidden="true">
    <polygon points="0,0 592,0 552,392 0,392" fill="var(--navy)"/>
    <polygon points="592,0 1200,0 1200,411 548,411" fill="var(--blue)"/>
  </svg>
  <section>
    <div class="abs tag-row" style="left:31px;top:1185px;">
      <div class="section-tag light">63,000 SAVED IN 40'S</div><div class="badge">$</div>
    </div>
    <ul class="abs bullets on-dark" style="left:31px;top:1305px;width:530px;">
      <li>Average american has 4k in liquid savings and 63k in retirement funds</li>
    </ul>

    <div class="abs tag-row" style="left:602px;top:1185px;">
      <div class="section-tag light">6X-8X SALARY SAVED</div><div class="badge">$</div>
    </div>
    <ul class="abs bullets on-blue" style="left:600px;top:1307px;width:560px;">
      <li>Have 6x-8x annual salary saved by retirement</li>
      <li>Average American has 5k in liquid savings &amp; 117k in retirement funds</li>
      <li>Dont remove investments from stocks too much, but diversify further</li>
    </ul>
  </section>

  <section>
    <h2 class="abs headline" style="left:30px;top:1538px;">250,000? IS WHAT SHOULD BE SAVED</h2>
    <ul class="abs bullets" style="left:31px;top:1648px;width:600px;">
      <li>Use HSA or FSA accounts</li>
      <li>Life insurance bought and understood</li>
    </ul>
  </section>

  <section>
    <div class="abs tag-row" style="left:31px;top:1756px;">
      <div class="section-tag">INVESTING IN YOUR 60'S</div><div class="badge">$</div>
    </div>
    <div class="abs stat" style="left:28px;top:1860px;">
      <span class="stat-figure" style="font-size:118px;">10X</span>
      <span class="stat-note" style="margin-left:22px;">Stay the course - Have 8x annual salary by 60 and 10x by 67</span>
    </div>
    <ul class="abs bullets" style="left:31px;top:1978px;width:960px;">
      <li>Average american has 8k in liquid savings and median retirement account value of 172k</li>
      <li>Average social security benefit is only 1.4k (Need more SSA info Dana)</li>
      <li>Understand required minimum distribution (RMD) - differences between 401k and IRAs</li>
      <li>Life expectancy and preparing for that</li>
      <li>May need to work longer</li>
      <li>Downsize</li>
    </ul>
  </section>

  <h2 class="abs headline" style="left:30px;top:2238px;">OVERALL INVESTING INFORMATION</h2>
  <svg class="abs closing" viewBox="0 0 1200 624" aria-hidden="true">
    <polygon points="1166,3 1166,511 266,511" fill="var(--navy)"/>
    <polygon points="28,113 935,113 266,511 28,623" fill="var(--blue)"/>
    <circle cx="146" cy="330" r="33" fill="var(--white)"/>
    <path d="M84 440 v-25 a40 40 0 0 1 40 -40 h46 a40 40 0 0 1 40 40 v25 z" fill="var(--white)"/>
    <circle cx="231" cy="428" r="52" fill="var(--blue)"/>
    <circle cx="231" cy="428" r="45" fill="var(--white)"/>
    <text x="231" y="449" text-anchor="middle" font-family="Anton, sans-serif" font-size="58" fill="var(--blue)">$</text>
    <g fill="none" stroke="var(--white)" stroke-width="10">
      <rect x="970" y="178" width="110" height="28" rx="14"/>
      <rect x="970" y="214" width="110" height="28" rx="14"/>
      <rect x="970" y="250" width="110" height="28" rx="14"/>
      <rect x="970" y="286" width="110" height="28" rx="14"/>
      <rect x="970" y="322" width="110" height="28" rx="14"/>
    </g>
    <circle cx="955" cy="280" r="72" fill="var(--navy)" stroke="var(--white)" stroke-width="11"/>
    <text x="955" y="310" text-anchor="middle" font-family="Anton, sans-serif" font-size="82" fill="var(--white)">$</text>
  </svg>
  <section>
    <div class="abs big-white" style="left:55px;top:2386px;">56%</div>
    <p class="abs white-note" style="left:291px;top:2396px;width:360px;">Of households currently have money in an employer-sponsored retirement account (including pensions, 401(k)s, and others).</p>
    <div class="abs big-white" style="left:540px;top:2628px;">35%</div>
    <p class="abs white-note" style="left:777px;top:2648px;width:340px;">Americans don't participate in any retirement savings plan at all.</p>
  </section>

</body>
</html>
```